Corvena Hotel, city center modern minimal hotel operating all year round, on Rhodes island Greece

city, modern ,all year operating hotel

Target Market(s)

tourists, business agents

Industry/Entity Type

tourism

Coding

Coded - Design and coding required

Number of Pages Required

2 page

Requirements
Must have
• room type photos and descriptions, amenities individual listing (graphic), comments sections, map driving location details
Nice to have
• gallery section, modern and minimal design, amenities section, individual room type descriptions, photos and facilities

```html
<!DOCTYPE html>
<html lang="en">
<head>
<meta charset="utf-8">
<title>Corvena Hotel – Rhodes</title>
<link href="https://fonts.googleapis.com/css2?family=Lora:ital,wght@0,400;0,500;0,700;1,400&family=Arimo:wght@400;700&display=swap" rel="stylesheet">
<style>
:root{
  --gold:#c39a3b;
  --gold-dark:#a8822c;
  --green:#1d4a33;
  --green-deep:#173d2a;
  --cream:#fcf8ee;
  --ink:#333;
  --muted:#555;
  --white:#fff;
  --line:#e6e0d2;
}
*{box-sizing:border-box;margin:0;padding:0}
html,body{width:1200px;height:5059px;overflow:hidden}
body{position:relative;font-family:'Arimo',Arial,sans-serif;color:var(--ink);background:var(--white)}
.serif{font-family:'Lora',Georgia,serif}
section,header,footer{position:absolute;left:0;width:1200px}
.abs{position:absolute}
.center{left:0;width:1200px;text-align:center}
.section-title{font-family:'Lora',Georgia,serif;font-weight:400;color:var(--green);font-size:36px;letter-spacing:.5px}
.title-rule{position:absolute;left:575px;width:50px;height:3px;background:var(--green)}

/* hero */
.hero{top:0;height:807px;background:radial-gradient(ellipse at 55% 45%,#6d5537 0%,#3e2d1c 55%,#1f160e 100%)}
.brand{position:absolute;display:flex;align-items:center;gap:12px;color:var(--white);font-family:'Lora',Georgia,serif;font-weight:400;letter-spacing:2px;white-space:nowrap}
.brand .mark{width:22px;height:22px;border:2px solid var(--white);transform:rotate(45deg)}
.hero .brand{left:112px;top:40px;font-size:34px}
.nav{position:absolute;top:55px;font-family:'Lora',Georgia,serif;font-size:14px;color:var(--white)}
.nav.active::after{content:"";position:absolute;left:0;right:0;top:30px;height:2px;background:var(--gold)}
.btn-book{position:absolute;left:947px;top:39px;width:139px;height:49px;border-radius:25px;background:var(--gold);color:var(--white);font-family:'Lora',Georgia,serif;font-size:14px;display:flex;align-items:center;justify-content:center}
.hero-kicker{top:328px;font-family:'Lora',Georgia,serif;font-size:17px;color:#f2e6cf}
.hero-title{top:360px;font-family:'Lora',Georgia,serif;font-weight:700;font-size:74px;line-height:82px;color:var(--white)}
.btn-outline{position:absolute;left:518px;top:548px;width:165px;height:49px;border:2px solid var(--gold);border-radius:25px;color:var(--white);font-family:'Lora',Georgia,serif;font-size:15px;display:flex;align-items:center;justify-content:center}

/* welcome */
.welcome{top:807px;height:745px;background:linear-gradient(#f6f8fb,#fff 120px)}
.welcome-kicker{top:52px;font-family:'Lora',Georgia,serif;font-size:22px;color:var(--green)}
.welcome-name{top:85px;font-family:'Lora',Georgia,serif;font-weight:400;font-size:48px;color:var(--gold)}
.welcome-text{top:152px;text-align:center;font-size:12.5px;line-height:26px;color:var(--ink);white-space:nowrap}
.diamond{position:absolute;top:271px;width:360px;height:407px}
.diamond svg{position:absolute;left:0;top:0}
.diamond .d-icon{position:absolute;left:150px;top:70px}
.diamond h3{position:absolute;left:0;width:360px;top:160px;text-align:center;font-family:'Lora',Georgia,serif;font-weight:400;font-size:23px;color:var(--white)}
.diamond p{position:absolute;left:0;width:360px;top:198px;text-align:center;font-size:12px;line-height:26px;color:#fff;white-space:nowrap}
.diamond .go{position:absolute;left:158px;top:292px;width:44px;height:44px;border-radius:50%;display:flex;align-items:center;justify-content:center}

/* rooms */
.rooms{top:1552px;height:811px;background:var(--cream)}
.room-card{position:absolute;top:145px;width:308px;height:587px;background:var(--white);border:1px solid var(--line)}
.room-photo{height:248px;background:linear-gradient(135deg,#8a7a66,#3b3128)}
.room-card h4{margin-top:34px;text-align:center;font-family:'Lora',Georgia,serif;font-weight:700;font-size:15px;color:#222}
.stars{margin-top:6px;text-align:center;color:var(--gold);font-size:16px;letter-spacing:3px}
.specs{margin:34px 0 0 36px;font-family:'Lora',Georgia,serif;font-size:12.5px;color:#333}
.specs div{display:flex;height:33.5px}
.specs span:nth-child(1){width:100px}
.specs span:nth-child(2){width:38px}
.btn-details{margin:20px auto 0;width:143px;height:47px;border:1.5px solid var(--gold);border-radius:24px;color:var(--gold);font-family:'Lora',Georgia,serif;font-size:13px;display:flex;align-items:center;justify-content:center}
.arrow-btn{position:absolute;top:397px;width:54px;height:54px;border-radius:50%;border:1.5px solid #bbb;background:var(--white);display:flex;align-items:center;justify-content:center}

/* booking */
.booking{top:2363px;height:479px;background:var(--gold)}
.booking .section-title{color:var(--white)}
.field-label{position:absolute;font-family:'Lora',Georgia,serif;font-size:11.5px;color:var(--white)}
.field{position:absolute;height:47px;background:var(--white);border-radius:4px}
.field svg{position:absolute;right:14px;top:17px}
.btn-send{position:absolute;left:511px;top:389px;width:177px;height:53px;border-radius:27px;background:var(--green);color:var(--white);font-family:'Lora',Georgia,serif;font-weight:700;font-size:15px;display:flex;align-items:center;justify-content:center}

/* gallery */
.gallery{top:2842px;height:752px}
.shot{position:absolute;width:313px;height:256px}

/* testimonials */
.testimonials{top:3594px;height:403px;background:var(--cream)}
.band{top:3997px;height:69px;background:#f1efea}
.portrait{position:absolute;left:134px;top:52px;width:360px;height:360px;border-radius:50%;background:radial-gradient(circle at 50% 40%,#e2c9a0,#b88a4c 70%,#8a6a3a)}
.quote{position:absolute;left:560px;top:170px;font-family:'Lora',Georgia,serif;font-style:italic;font-size:13.5px;line-height:26px;color:#555;white-space:nowrap}
.author{position:absolute;left:560px;top:324px;font-family:'Lora',Georgia,serif;font-size:17px;color:#444}
.author b{color:var(--green)}

/* contact */
.contact{top:4066px;height:549px}
.map{position:absolute;left:208px;top:121px;width:784px;height:375px;background:linear-gradient(#eef2f7,#e3e8ee)}

/* footer */
.footer{top:4615px;height:444px;background:var(--green-deep)}
.footer .brand{left:0;width:1200px;justify-content:center;top:72px;font-size:44px}
.footer-nav{position:absolute;top:173px;font-family:'Lora',Georgia,serif;font-size:14px;color:var(--white)}
.info-icon{position:absolute;top:226px;width:70px;height:70px;border-radius:50%;border:2px solid var(--gold);display:flex;align-items:center;justify-content:center}
.info-text{position:absolute;top:313px;width:300px;text-align:center;font-family:'Lora',Georgia,serif;font-size:14px;color:var(--white)}
.social{position:absolute;top:392px;width:34px;height:34px;border-radius:50%;border:1.5px solid var(--white)}
.copyright{position:absolute;right:90px;top:399px;font-family:'Lora',Georgia,serif;font-size:15px;color:var(--white)}
.live-chat{position:absolute;left:1145px;top:4725px;width:55px;height:189px;background:var(--gold);border-radius:8px 0 0 8px;display:flex;align-items:center;justify-content:center}
.live-chat span{transform:rotate(-90deg);white-space:nowrap;color:var(--white);font-weight:700;font-size:14px}
</style>
</head>
<body>

<header class="hero" role="img" aria-label="Hotel bedroom interior with bed, lamp and desk in warm evening light">
  <div class="brand"><span class="mark"></span>CORVENA HOTEL</div>
  <span class="nav active" style="left:538px">HOME</span>
  <span class="nav" style="left:632px">ROOMS</span>
  <span class="nav" style="left:736px">GALLERY</span>
  <span class="nav" style="left:850px">CONTACT</span>
  <span class="btn-book">BOOK NOW</span>
  <div class="abs center hero-kicker">INDOOR &amp; OUTDOOR</div>
  <h1 class="abs center hero-title">ENJOY LUXURY<br>EXPERIENCE</h1>
  <span class="btn-outline">LEARN MORE</span>
</header>

<section class="welcome">
  <div class="abs center welcome-kicker">WELCOME TO</div>
  <h2 class="abs center welcome-name">CORVENA HOTEL</h2>
  <p class="abs center welcome-text">The hotel is renowned in the local market due to its operation which “runs” 365 days a year. All rooms have been<br>renovated recently and offer a unique design with modern furnishes. Being in constant operation for the last 47<br>through numerous renovations the hotel operates mainly with repeaters</p>

  <div class="diamond" style="left:92px">
    <svg width="360" height="407"><polygon points="180,0 360,203 180,407 0,203" fill="var(--gold)"/></svg>
    <svg class="d-icon" width="60" height="60" viewBox="0 0 60 60" fill="none" stroke="#fff" stroke-width="2"><path d="M30 50 C10 35 6 24 12 16 C18 9 26 12 30 19 C34 12 42 9 48 16 C54 24 50 35 30 50Z"/></svg>
    <h3>FRIENDLINESS</h3>
    <p>The hotel offers its services to<br>both local and international guests<br>either family or business type.</p>
    <span class="go" style="background:var(--green)"><svg width="14" height="14"><path d="M5 2 L10 7 L5 12" stroke="#fff" stroke-width="2" fill="none"/></svg></span>
  </div>
  <div class="diamond" style="left:419px">
    <svg width="360" height="407"><polygon points="180,0 360,203 180,407 0,203" fill="var(--green)"/></svg>
    <svg class="d-icon" width="60" height="60" viewBox="0 0 60 60" fill="none" stroke="#fff" stroke-width="2"><path d="M30 54 C18 38 14 30 14 22 A16 16 0 0 1 46 22 C46 30 42 38 30 54Z"/><circle cx="30" cy="22" r="6"/></svg>
    <h3>LOCATION</h3>
    <p>Medieval city is just a few steps<br>away, so are the beautiful beaches of<br>Elli and Psaropoula.</p>
    <span class="go" style="background:var(--gold);top:304px;width:56px;height:56px;left:152px"><svg width="14" height="14"><path d="M5 2 L10 7 L5 12" stroke="#fff" stroke-width="2" fill="none"/></svg></span>
  </div>
  <div class="diamond" style="left:714px">
    <svg width="360" height="407"><polygon points="180,0 360,203 180,407 0,203" fill="var(--gold)"/></svg>
    <svg class="d-icon" width="60" height="60" viewBox="0 0 60 60" fill="none" stroke="#fff" stroke-width="2"><circle cx="22" cy="18" r="7"/><circle cx="40" cy="18" r="7"/><path d="M8 50 C8 34 36 34 36 50"/><path d="M28 36 C40 30 54 36 54 50"/></svg>
    <h3>AMENITIES</h3>
    <p>The hotel offers most modern<br>amenities, like satellite television set,<br>mini bar, en sure bathroom</p>
    <span class="go" style="background:var(--green)"><svg width="14" height="14"><path d="M5 2 L10 7 L5 12" stroke="#fff" stroke-width="2" fill="none"/></svg></span>
  </div>
</section>

<section class="rooms">
  <h2 class="abs center section-title" style="top:52px">OUR ROOMS &amp; SUITES</h2>
  <span class="title-rule" style="top:113px"></span>
  <span class="arrow-btn" style="left:38px"><svg width="14" height="14"><path d="M9 2 L4 7 L9 12" stroke="#333" stroke-width="2" fill="none"/></svg></span>
  <span class="arrow-btn" style="left:1102px"><svg width="14" height="14"><path d="M5 2 L10 7 L5 12" stroke="#333" stroke-width="2" fill="none"/></svg></span>

  <article class="room-card" style="left:112px">
    <div class="room-photo" role="img" aria-label="Apartment living room with grey sofa and lit wall panel" style="background:linear-gradient(135deg,#d9dde3,#6b7280)"></div>
    <h4>APARTMENT FOR 4 ADULTS</h4>
    <div class="stars">★★★★★</div>
    <div class="specs"><div><span>BEDROOM</span><span>:</span><span>1 DOUBLE BED</span></div><div><span>BEDROOM</span><span>:</span><span>2 SINGLE BEDS</span></div><div><span>LIVING ROOM</span><span>:</span><span>1 SOFA BED</span></div><div><span>APARTMENT</span><span>:</span><span>60 M2</span></div></div>
    <span class="btn-details">VIEW DETAILS</span>
  </article>
  <article class="room-card" style="left:446px">
    <div class="room-photo" role="img" aria-label="Superior double room with striped cushions and wooden screen"></div>
    <h4>SUPERIOR DOUBLE ROOM</h4>
    <div class="stars">★★★★★</div>
    <div class="specs"><div><span>BEDROOM</span><span>:</span><span>1 DOUBLE BED</span></div><div><span>BEDROOM</span><span>:</span><span>2 SINGLE BEDS</span></div><div><span>LIVING ROOM</span><span>:</span><span>1 SOFA BED</span></div><div><span>APARTMENT</span><span>:</span><span>60 M2</span></div></div>
    <span class="btn-details">VIEW DETAILS</span>
  </article>
  <article class="room-card" style="left:778px">
    <div class="room-photo" role="img" aria-label="Quadruple room with dark bed and framed artwork" style="background:linear-gradient(135deg,#6e5c45,#241b13)"></div>
    <h4>QUADRUPLE ROOM</h4>
    <div class="stars">★★★★★</div>
    <div class="specs"><div><span>BEDROOM</span><span>:</span><span>1 DOUBLE BED</span></div><div><span>BEDROOM</span><span>:</span><span>2 SINGLE BEDS</span></div><div><span>LIVING ROOM</span><span>:</span><span>1 SOFA BED</span></div><div><span>APARTMENT</span><span>:</span><span>60 M2</span></div></div>
    <span class="btn-details">VIEW DETAILS</span>
  </article>
</section>

<section class="booking">
  <h2 class="abs center section-title" style="top:44px">CORVENA CITY HOTEL RHODES</h2>
  <span class="title-rule" style="top:99px;background:var(--white)"></span>
  <div class="abs center serif" style="top:118px;font-size:13px;color:#fff">ONE OF THE BEST PLACES TO RELAX &amp; ENJOY</div>

  <span class="field-label" style="left:112px;top:184px">FULL NAME*</span>
  <span class="field-label" style="left:444px;top:184px">EMAIL*</span>
  <span class="field-label" style="left:774px;top:184px">PHONE*</span>
  <span class="field" style="left:112px;top:210px;width:312px"></span>
  <span class="field" style="left:444px;top:210px;width:310px"></span>
  <span class="field" style="left:774px;top:210px;width:312px"></span>

  <span class="field-label" style="left:112px;top:279px">ARRIVAL DATE*</span>
  <span class="field-label" style="left:403px;top:279px">DEPARTURE DATE*</span>
  <span class="field-label" style="left:695px;top:279px">ROOMS*</span>
  <span class="field-label" style="left:825px;top:279px">ADULTS*</span>
  <span class="field-label" style="left:972px;top:279px">CHILDREN</span>
  <span class="field" style="left:112px;top:304px;width:279px"><svg width="12" height="12"><rect x="1" y="2" width="10" height="9" fill="none" stroke="#666"/><line x1="1" y1="5" x2="11" y2="5" stroke="#666"/></svg></span>
  <span class="field" style="left:403px;top:304px;width:273px"><svg width="12" height="12"><rect x="1" y="2" width="10" height="9" fill="none" stroke="#666"/><line x1="1" y1="5" x2="11" y2="5" stroke="#666"/></svg></span>
  <span class="field" style="left:695px;top:304px;width:116px"><svg width="10" height="10"><path d="M1 3 L5 7 L9 3Z" fill="#444"/></svg></span>
  <span class="field" style="left:825px;top:304px;width:133px"><svg width="10" height="10"><path d="M1 3 L5 7 L9 3Z" fill="#444"/></svg></span>
  <span class="field" style="left:972px;top:304px;width:114px"><svg width="10" height="10"><path d="M1 3 L5 7 L9 3Z" fill="#444"/></svg></span>
  <span class="btn-send">SEND</span>
</section>

<section class="gallery">
  <h2 class="abs center section-title" style="top:56px">PHOTO GALLERY</h2>
  <span class="title-rule" style="top:117px"></span>
  <div class="shot" role="img" aria-label="Bright bedroom with white bed" style="left:112px;top:147px;background:linear-gradient(135deg,#e8e8ea,#7c7a78)"></div>
  <div class="shot" role="img" aria-label="Kitchen and dining area" style="left:442px;top:147px;background:linear-gradient(135deg,#d8cbb2,#5a4b3a)"></div>
  <div class="shot" role="img" aria-label="Rooftop terrace with hot tub" style="left:774px;top:147px;background:linear-gradient(135deg,#9fb3c8,#4a4036)"></div>
  <div class="shot" role="img" aria-label="Double room with striped cushions" style="left:112px;top:416px;background:linear-gradient(135deg,#8c7a63,#2e251c)"></div>
  <div class="shot" role="img" aria-label="Bathroom with wooden vanity" style="left:442px;top:416px;background:linear-gradient(135deg,#9a8872,#3a2e24)"></div>
  <div class="shot" role="img" aria-label="Bedroom with framed artwork above bed" style="left:774px;top:416px;background:linear-gradient(135deg,#7a6546,#1e1710)"></div>
</section>

<section class="testimonials">
  <div class="portrait" role="img" aria-label="Guest with a suitcase in the hotel lobby"></div>
  <h2 class="abs section-title" style="left:554px;top:82px;font-size:36px">TESTIMONIALS</h2>
  <p class="quote">Nikos Welcomed us with a very generous touch, Authentic Greek<br>Hospitality, If you want to experience a genuine village experience<br>with the community, and savor the magnificent viewing in the<br>streets, like postal cards, well this is the right place away from the<br>touristic crowd, I loved it!!</p>
  <div class="author"><b>Julien</b> Lebanon</div>
</section>
<section class="band"></section>

<section class="contact">
  <h2 class="abs center section-title" style="top:44px">CONTACT US</h2>
  <div class="map" role="img" aria-label="Street map of Rhodes town with the hotel location marked"></div>
</section>

<footer class="footer">
  <div class="brand"><span class="mark"></span>CORVENA HOTEL</div>
  <span class="footer-nav" style="left:406px">HOME</span>
  <span class="footer-nav" style="left:502px">ROOMS</span>
  <span class="footer-nav" style="left:604px">GALLERY</span>
  <span class="footer-nav" style="left:718px">CONTACT</span>

  <span class="info-icon" style="left:214px"><svg width="22" height="26" viewBox="0 0 22 26"><path d="M11 25 C4 16 2 12 2 9 A9 9 0 0 1 20 9 C20 12 18 16 11 25Z" fill="#fff"/><circle cx="11" cy="9" r="3.5" fill="var(--green-deep)"/></svg></span>
  <span class="info-icon" style="left:466px"><svg width="22" height="22" viewBox="0 0 22 22"><path d="M5 2 L9 2 L10 7 L7 9 C8.5 12 10 13.5 13 15 L15 12 L20 13 L20 17 C20 19 18 20 16 20 C8 19 3 14 2 6 C2 4 3 2 5 2Z" fill="#fff"/></svg></span>
  <span class="info-icon" style="left:713px"><svg width="24" height="18" viewBox="0 0 24 18"><rect x="1" y="1" width="22" height="16" rx="2" fill="#fff"/><path d="M1 2 L12 10 L23 2" stroke="var(--green-deep)" stroke-width="2" fill="none"/></svg></span>
  <span class="info-icon" style="left:955px"><svg width="22" height="22" viewBox="0 0 22 22"><circle cx="11" cy="11" r="10" fill="#fff"/><path d="M1 11 H21 M11 1 C6 6 6 16 11 21 M11 1 C16 6 16 16 11 21" stroke="var(--green-deep)" stroke-width="1.5" fill="none"/></svg></span>
  <span class="info-text" style="left:99px">14 Harbour Lane, Rhodes 851 00</span>
  <span class="info-text" style="left:351px">(+30) 2241055190</span>
  <span class="info-text" style="left:598px">info@corvenahotel.gr</span>
  <span class="info-text" style="left:840px">corvenahotel.gr</span>

  <span class="social" style="left:115px"></span>
  <span class="social" style="left:157px"></span>
  <span class="social" style="left:199px"></span>
  <span class="social" style="left:241px"></span>
  <span class="social" style="left:285px"></span>
  <span class="copyright">© Copyright 2022 Corvena Hotel.All Rights Reserved</span>
</footer>

<div class="live-chat"><span>LIVE CHAT</span></div>

</body>
</html>
```